Residential building / Apartments for sale landing page

I need a website / landing page design for my latest development project - a residential building with 70+ apartments for sale. I need the design in layers in Photoshop/Illustrator/InDesign format with all the icons/shapes/maps/graphic assets in vector format (svg, ai, eps) as much as possible.

I prefer white website and please consider the performance/coding experience. We're not making something suitable only for a design contest with fancy parallax effects and confusing animations. We're trying to create usable and clean UI with good UX.

The website will be custom coded, i.e. I'm not using WordPress.

I know that the existing 3D photos are not good but for now you can use them or replace them with some stock photos. I'm going to create new 3D photos soon.

Industry/Entity Type

Real Estate Development

Number of Pages Required

1 page

```html
<!DOCTYPE html>
<html lang="en">
<head>
<meta charset="utf-8">
<title>Pine Heights – Apartments for Sale</title>
<link rel="stylesheet" href="https://fonts.googleapis.com/css2?family=Arvo:wght@400;700&family=Arimo:ital,wght@0,400;0,700;1,400;1,700&display=swap">
<style>
:root{
  --green:#88c43f;
  --green-dark:#6fa82e;
  --ink:#333335;
  --muted:#5b5b5e;
  --paper:#ffffff;
  --page:#f8f8f8;
  --night:#2d2c30;
  --footer:#262425;
  --line:#d5d5d5;
}
*{box-sizing:border-box;margin:0;padding:0}
html,body{width:1200px;height:4000px;overflow:hidden}
body{position:relative;background:var(--page);font-family:"Arimo",Arial,sans-serif;color:var(--ink)}
.abs{position:absolute}
.slab{font-family:"Arvo",Georgia,serif;font-weight:700}

/* header */
.hero{left:0;top:0;width:1200px;height:812px;background:linear-gradient(100deg,#f3f3f1 0%,#e6e8e6 30%,#d9dad8 55%,#c9c8c6 75%,#e8e6e2 100%)}
.hero-bar{left:87px;top:804px;width:1025px;height:8px;background:var(--green)}
.top-contact{left:877px;top:15px;font-size:10px;color:#444}
.lang{left:963px;top:9px;width:149px;height:26px;border:1.5px solid #777;border-radius:4px;background:#f4f4f4;font-size:9px;color:#444;padding:6px 0 0 8px}
.lang i{display:inline-block;width:12px;height:8px;background:#666;margin-right:5px;vertical-align:-1px}
.lang b{position:absolute;right:8px;top:8px;width:14px;height:9px;border-radius:2px;background:linear-gradient(#c0392b 33%,#fff 33% 66%,#2c4a9a 66%)}
.nav{left:87px;top:47px;width:1025px;height:71px;background:var(--green);border-radius:2px}
.logo{left:22px;top:24px;color:#fff;font-weight:700;font-size:17px;letter-spacing:.5px;display:flex;align-items:center;gap:8px}
.logo span.mark{width:14px;height:14px;border-radius:50%;background:#fff}
.menu{right:28px;top:27px;display:flex;gap:21px;font-size:11.5px;font-weight:700;letter-spacing:.6px;color:#fff}
.menu a:first-child{color:#2c2c2c}
.menu a{text-decoration:none;color:inherit}
.hero-title{left:87px;top:246px;font-size:50px;line-height:46px;color:var(--green);letter-spacing:6px}
.hero-sub{left:87px;top:362px;font-size:21px;line-height:33px;font-weight:700;letter-spacing:3.5px;color:#3a3a3a}
.price{left:87px;top:626px;font-size:17px;letter-spacing:2px;color:#3a3a3a;display:flex;align-items:center;gap:10px}
.price .tag{background:var(--green);color:#fff;font-style:italic;font-weight:700;padding:1px 14px;border-radius:11px;letter-spacing:1px}

/* apartment strip */
.card{top:879px;width:323px;height:200px;background:var(--paper);box-shadow:0 1px 4px rgba(0,0,0,.08);overflow:hidden}
.card .ph{height:139px;background:linear-gradient(90deg,#e9e7e3 0%,#f4f2ee 45%,#d9c4a3 70%,#b99a72 100%)}
.card .ph.warm{background:linear-gradient(90deg,#a77d4e 0%,#e9e4da 40%,#7fa7a4 70%,#c9a57a 100%)}
.card p{padding:14px 16px 0;font-size:11.5px;line-height:22px;color:#555;letter-spacing:.4px}

/* amenities */
.amen{left:0;top:1144px;width:1200px;height:453px;background:linear-gradient(90deg,#8cc744 0%,#86c23e 55%,#7fba3a 100%)}
.amen-photo{left:87px;top:1209px;width:498px;height:278px;border:4px solid #fff;background:linear-gradient(180deg,#c8d7e8 0%,#d9e4ef 40%,#9fb3c8 60%,#4b7a3a 85%,#3e6b2f 100%)}
.amen-h{left:702px;top:1204px;font-size:23px;line-height:29px;color:#fff}
.amen-list{top:1283px;font-size:11.5px;line-height:22.2px;color:#fff;letter-spacing:.5px;list-style:none}
.amen-list b{font-style:italic;margin-right:4px}
.amen-icon{left:701px;top:1471px}
.amen-t{left:789px;top:1477px;font-size:11px;font-weight:700;letter-spacing:1.2px;color:#fff}
.amen-p{left:789px;top:1497px;width:330px;font-size:11.5px;line-height:22px;color:#fff;letter-spacing:.4px}

/* specs */
.specs-h{left:87px;top:1656px;font-size:23px;line-height:29px;color:var(--green)}
.spec-n{font-family:"Arimo",sans-serif;font-style:italic;font-weight:700;font-size:31px;letter-spacing:3px;color:#222}
.spec-img{width:88px;height:42px;background:linear-gradient(90deg,#e6e1d8,#f2efe9 50%,#b89466)}
.spec-t{width:295px;font-size:11.5px;line-height:17px;color:#444;letter-spacing:.4px}

/* location */
.loc{left:0;top:2184px;width:1200px;height:674px;background:linear-gradient(180deg,#3a393d 0%,#2f2e32 50%,#29282b 100%)}
.loc-h{left:87px;top:2245px;font-size:23px;color:var(--green)}
.loc-p{left:87px;top:2295px;width:420px;font-size:11.5px;line-height:17px;color:#e6e6e6;letter-spacing:.4px}
.map{left:87px;top:2353px;width:1025px;height:441px;background:linear-gradient(135deg,#efe6d3 0%,#cfe3c2 35%,#eee4cf 55%,#b9d9a8 75%,#ece3cd 100%)}

/* gallery */
.gal-h{left:87px;top:2919px;font-size:23px;color:var(--green)}
.gal-p{left:87px;top:2968px;width:230px;font-size:11.5px;line-height:22px;color:#555;letter-spacing:.4px}
.g{width:236px;height:234px;background:#fff;box-shadow:0 1px 5px rgba(0,0,0,.08)}
.g .ph{height:180px;background:linear-gradient(180deg,#eeece8 0%,#e9e6e0 62%,#c39c69 63%,#a8814f 78%,#d7d1c6 79%)}
.g .ph.dining{background:linear-gradient(90deg,#9a6f45 0%,#e7e3da 30%,#86aaa6 60%,#b48b5d 100%)}
.g h4{position:absolute;left:14px;top:193px;font-size:11.5px;letter-spacing:1.3px;color:#333}
.g small{position:absolute;left:14px;top:212px;font-size:11px;font-style:italic;color:#777;letter-spacing:.6px}
.g .btn{position:absolute;right:14px;top:197px;width:74px;height:22px;border-radius:3px;background:var(--green);color:#fff;font-size:11px;font-weight:700;display:flex;align-items:center;justify-content:center;gap:5px;letter-spacing:.6px}
.more{left:952px;top:3300px;font-size:11.5px;letter-spacing:.8px;color:#444;display:flex;align-items:center;gap:6px}

/* footer */
.foot{left:0;top:3487px;width:1200px;height:465px;background:var(--footer)}
.foot-h{top:3545px;font-size:23px;color:var(--green)}
.foot-p{left:87px;width:330px;font-size:11.5px;line-height:22px;color:#e5e5e5;letter-spacing:.4px}
.foot-p.intro{width:322px}
.field{height:24px;border-bottom:1px solid #8a8a8a;font-size:11px;font-weight:700;letter-spacing:.8px;color:#e8e8e8}
.send{left:613px;top:3850px;width:148px;height:36px;background:var(--green);color:#fff;font-size:11.5px;font-weight:700;letter-spacing:.8px;display:flex;align-items:center;justify-content:center;gap:6px}
.base{left:0;top:3952px;width:1200px;height:48px;background:var(--green)}
.social{left:87px;top:16px;display:flex;gap:7px}
.social i{width:12px;height:12px;background:#fff;border-radius:2px;display:block}
.copy{left:0;width:1200px;top:17px;text-align:center;font-size:11px;color:#fff;letter-spacing:.8px}
</style>
</head>
<body>

<!-- hero -->
<div class="abs hero" role="img" aria-label="Photo of a smiling woman relaxing in a grey lounge chair by a bright window with a potted plant"></div>
<div class="abs hero-bar"></div>
<div class="abs top-contact">Contact</div>
<div class="abs lang"><i></i>Language<b></b></div>
<nav class="abs nav">
  <div class="abs logo"><span class="mark"></span>PINE HEIGHTS</div>
  <div class="abs menu"><a>Pine Heights</a><a>The project</a><a>Apartments/ Sales</a><a>Location</a><a>Gallery</a></div>
</nav>
<h1 class="abs slab hero-title">SALE OF<br>APARTMENTS</h1>
<p class="abs hero-sub">DIRECTLY FROM THE INVESTOR<br>WITH 10% DISCOUNT</p>
<p class="abs price">PRICE FROM <span class="tag">9.999</span> EUR/M2</p>

<!-- apartment strip -->
<div class="abs card" style="left:-264px"><div class="ph" role="img" aria-label="Interior render of a living room"></div><p>Lorem ipsum dolor sit amet, consectetuer adipi-<br>scing elit, sed diam nonummy nibh euismod</p></div>
<div class="abs card" style="left:87px"><div class="ph" role="img" aria-label="Interior render of a living room with wooden slat partition"></div><p>Lorem ipsum dolor sit amet, consectetuer adipi-<br>scing elit, sed diam nonummy nibh euismod</p></div>
<div class="abs card" style="left:438px"><div class="ph warm" role="img" aria-label="Interior render of a dining room with wooden chairs"></div><p>Lorem ipsum dolor sit amet, consectetuer adipi-<br>scing elit, sed diam nonummy nibh euismod</p></div>
<div class="abs card" style="left:789px"><div class="ph" role="img" aria-label="Interior render of a living room with wooden slat partition"></div><p>Lorem ipsum dolor sit amet, consectetuer adipi-<br>scing elit, sed diam nonummy nibh euismod</p></div>
<div class="abs card" style="left:1140px"><div class="ph warm" role="img" aria-label="Interior render of a dining room"></div><p>Lorem i<br>scing e</p></div>

<!-- amenities -->
<section class="abs amen" role="img" aria-label="Green tinted background with faint trees and building"></section>
<div class="abs amen-photo" role="img" aria-label="Photo of a white apartment block with blue balconies behind trees"></div>
<h2 class="abs slab amen-h">Lorem ipsum dolor sit amet<br>consectetuer adipiscing</h2>
<ul class="abs amen-list" style="left:702px">
  <li><b>01.</b>Green areas and gardens</li><li><b>02.</b>Parking spaces</li><li><b>03.</b>Bicycle parking</li>
  <li><b>04.</b>Outside workout area</li><li><b>05.</b>NFC controlled access</li><li><b>06.</b>Outdoor Yoga area</li>
</ul>
<ul class="abs amen-list" style="left:907px">
  <li><b>07.</b>Relaxation area</li><li><b>08.</b>Childrens playground</li><li><b>09.</b>Pool</li>
  <li><b>10.</b>Restaurant</li><li><b>11.</b>Etc.</li>
</ul>
<svg class="abs amen-icon" width="60" height="60" viewBox="0 0 60 60"><circle cx="30" cy="30" r="30" fill="#fff"/><path d="M30 12 L39 25 H35 L42 35 H37 L44 44 H16 L23 35 H18 L25 25 H21 Z" fill="#88c43f"/><rect x="28" y="44" width="4" height="6" fill="#88c43f"/></svg>
<div class="abs amen-t">HEADLINE LOREM IPSUM DOLOR</div>
<p class="abs amen-p">Lorem ipsum dolor sit amet, consectetuer adipiscing elit, sed diam nonummy</p>

<!-- specs -->
<h2 class="abs slab specs-h">Lorem ipsum dolor sit amet<br>consectetuer</h2>

<div class="abs spec-n" style="left:59px;top:1757px">01.</div><div class="abs spec-img" style="left:87px;top:1771px" role="img" aria-label="Interior thumbnail"></div>
<p class="abs spec-t" style="left:199px;top:1770px">Norvek Windows - 5 chamber noise reducing glazing with high temperature and noise insula-tion efficiency.</p>
<div class="abs spec-n" style="left:59px;top:1856px">02.</div><div class="abs spec-img" style="left:87px;top:1870px" role="img" aria-label="Interior thumbnail"></div>
<p class="abs spec-t" style="left:199px;top:1869px">Kallstein bricks - Austrian Kallstein Thermobrix bricks with porous system and 25 cm thick outer walls.</p>
<div class="abs spec-n" style="left:59px;top:1954px">03.</div><div class="abs spec-img" style="left:87px;top:1968px" role="img" aria-label="Interior thumbnail"></div>
<p class="abs spec-t" style="left:199px;top:1969px">High Ceilings - 2.70m high ceilings giving the light and space you need.</p>
<div class="abs spec-n" style="left:59px;top:2053px">04.</div><div class="abs spec-img" style="left:87px;top:2067px" role="img" aria-label="Interior thumbnail"></div>
<p class="abs spec-t" style="left:199px;top:2068px">Thermal Insulation System Mauerwerk - Mauerwerk Sili-cone Plaster Thermal Insulation System 10 cm thick and 15 cm thick from the north walls.</p>

<div class="abs spec-n" style="left:585px;top:1757px">05.</div><div class="abs spec-img" style="left:613px;top:1771px" role="img" aria-label="Interior thumbnail"></div>
<p class="abs spec-t" style="left:725px;top:1770px">Air conditioners - All air conditioners piping sys-tems are installed - ready to plug in the inside and outside body of the aircon system.</p>
<div class="abs spec-n" style="left:585px;top:1856px">06.</div><div class="abs spec-img" style="left:613px;top:1870px" role="img" aria-label="Interior thumbnail"></div>
<p class="abs spec-t" style="left:725px;top:1869px">HPL ventilated facede Panelform GmbH - Sus-pended ventilated facade with highly pressed laminated panels by Panelform GmbH in wood color.</p>
<div class="abs spec-n" style="left:585px;top:1954px">07.</div><div class="abs spec-img" style="left:613px;top:1968px" role="img" aria-label="Interior thumbnail"></div>
<p class="abs spec-t" style="left:725px;top:1969px">Panoramic Levanta lifts overlooking the park - Giving you the everyday glimpse over the inside garden and putting a smile on your face.</p>
<div class="abs spec-n" style="left:585px;top:2053px">08.</div><div class="abs spec-img" style="left:613px;top:2067px" role="img" aria-label="Interior thumbnail"></div>
<p class="abs spec-t" style="left:725px;top:2068px">Waterproofing with PVC membrane Sealtec - PVC membrane with high puncture and tear resistance, UV resistance and vapor permeability.</p>

<!-- location -->
<section class="abs loc" role="img" aria-label="Dark tinted background photo of apartment buildings"></section>
<h2 class="abs slab loc-h">Location lorem ipsum dolor</h2>
<p class="abs loc-p">Lorem ipsum dolor sit amet, consectetuer adipiscing elit, sed diam nonummy nibh euismod tincidunt ut erat volutpat.</p>
<svg class="abs" style="left:1055px;top:2241px" width="52" height="70" viewBox="0 0 52 70"><path d="M26 0C11.6 0 0 11.4 0 25.6 0 44 26 70 26 70S52 44 52 25.6C52 11.4 40.4 0 26 0Z" fill="#88c43f"/><circle cx="26" cy="25" r="9.5" fill="#2f2e32"/></svg>
<div class="abs map" role="img" aria-label="Road map of the surrounding region showing the development location"></div>

<!-- gallery -->
<h2 class="abs slab gal-h">Gallery</h2>
<p class="abs gal-p">Lorem ipsum dolor sit amet, consec-tetuer adipiscing elit, sed diam nonum-my.</p>

<div class="abs g" style="left:351px;top:2925px"><div class="ph" role="img" aria-label="Living room with TV on wooden sideboard"></div><h4>LOREM IPSUM</h4><small>12 March 2021</small><span class="btn"><svg width="12" height="8" viewBox="0 0 12 8"><path d="M0 4C2 0.5 10 0.5 12 4 10 7.5 2 7.5 0 4Z" fill="#fff"/><circle cx="6" cy="4" r="1.8" fill="#88c43f"/></svg>View</span></div>
<div class="abs g" style="left:613px;top:2925px"><div class="ph dining" role="img" aria-label="Dining room with wooden chairs"></div><h4>LOREM IPSUM</h4><small>12 March 2021</small><span class="btn"><svg width="12" height="8" viewBox="0 0 12 8"><path d="M0 4C2 0.5 10 0.5 12 4 10 7.5 2 7.5 0 4Z" fill="#fff"/><circle cx="6" cy="4" r="1.8" fill="#88c43f"/></svg>View</span></div>
<div class="abs g" style="left:877px;top:2925px"><div class="ph" role="img" aria-label="Living room with TV on wooden sideboard"></div><h4>LOREM IPSUM</h4><small>12 March 2021</small><span class="btn"><svg width="12" height="8" viewBox="0 0 12 8"><path d="M0 4C2 0.5 10 0.5 12 4 10 7.5 2 7.5 0 4Z" fill="#fff"/><circle cx="6" cy="4" r="1.8" fill="#88c43f"/></svg>View</span></div>
<div class="abs g" style="left:87px;top:3190px"><div class="ph" role="img" aria-label="Living room with TV on wooden sideboard"></div><h4>LOREM IPSUM</h4><small>12 March 2021</small><span class="btn"><svg width="12" height="8" viewBox="0 0 12 8"><path d="M0 4C2 0.5 10 0.5 12 4 10 7.5 2 7.5 0 4Z" fill="#fff"/><circle cx="6" cy="4" r="1.8" fill="#88c43f"/></svg>View</span></div>
<div class="abs g" style="left:351px;top:3190px"><div class="ph dining" role="img" aria-label="Dining room with wooden chairs"></div><h4>LOREM IPSUM</h4><small>12 March 2021</small><span class="btn"><svg width="12" height="8" viewBox="0 0 12 8"><path d="M0 4C2 0.5 10 0.5 12 4 10 7.5 2 7.5 0 4Z" fill="#fff"/><circle cx="6" cy="4" r="1.8" fill="#88c43f"/></svg>View</span></div>
<div class="abs g" style="left:613px;top:3190px"><div class="ph" role="img" aria-label="Living room with TV on wooden sideboard"></div><h4>LOREM IPSUM</h4><small>12 March 2021</small><span class="btn"><svg width="12" height="8" viewBox="0 0 12 8"><path d="M0 4C2 0.5 10 0.5 12 4 10 7.5 2 7.5 0 4Z" fill="#fff"/><circle cx="6" cy="4" r="1.8" fill="#88c43f"/></svg>View</span></div>
<div class="abs more"><svg width="13" height="9" viewBox="0 0 12 8"><path d="M0 4C2 0.5 10 0.5 12 4 10 7.5 2 7.5 0 4Z" fill="#444"/><circle cx="6" cy="4" r="1.8" fill="#f8f8f8"/></svg>View More</div>

<!-- contact -->
<footer class="abs foot"></footer>
<h2 class="abs slab foot-h" style="left:87px">Contact Us</h2>
<p class="abs foot-p intro" style="top:3594px">Lorem ipsum dolor sit amet, consectetuer adipiscing elit, sed diam nonummy nibh euismod tincidunt ut erat volutpat.</p>
<p class="abs foot-p" style="top:3682px"><b>Address</b><br>Lorem ipsum dolores sit amet<br>Dolorest amet<br>United states</p>
<p class="abs foot-p" style="top:3794px;display:flex;align-items:center;gap:6px"><svg width="11" height="9" viewBox="0 0 11 9"><rect x=".5" y=".5" width="10" height="8" fill="none" stroke="#e5e5e5"/><path d="M.5 .5 5.5 5 10.5 .5" fill="none" stroke="#e5e5e5"/></svg>hello@pineheights-example.com</p>
<p class="abs foot-p" style="top:3816px;display:flex;align-items:center;gap:6px"><svg width="10" height="10" viewBox="0 0 10 10"><path d="M1 1.5 3 0.5 4.5 3 3.5 4C4.2 5.5 4.8 6 6 6.5L7 5.5 9.5 7 8.5 9C4.5 9 1 5.5 1 1.5Z" fill="#e5e5e5"/></svg>(0199) 555 0142</p>

<h2 class="abs slab foot-h" style="left:613px">Send Us A Message</h2>
<div class="abs field" style="left:613px;top:3596px;width:236px">First Name</div>
<div class="abs field" style="left:877px;top:3596px;width:235px">Last Name</div>
<div class="abs field" style="left:613px;top:3646px;width:236px">Phone Number</div>
<div class="abs field" style="left:877px;top:3646px;width:235px">E-mail Address</div>
<div class="abs field" style="left:613px;top:3696px;width:499px">Message</div>
<div class="abs send">Send <svg width="11" height="11" viewBox="0 0 11 11"><circle cx="5.5" cy="5.5" r="5.5" fill="#fff"/><path d="M4 3 6.5 5.5 4 8" fill="none" stroke="#88c43f" stroke-width="1.6"/></svg></div>

<div class="abs base">
  <div class="abs social" aria-label="Social links"><i></i><i></i><i></i><i></i><i></i><i></i></div>
  <div class="abs copy">© 2021 www.pineheights-example.com all rights reserved</div>
  <svg class="abs" style="left:1090px;top:13px" width="22" height="22" viewBox="0 0 22 22"><circle cx="11" cy="11" r="11" fill="#fff"/><path d="M11 16V6M6.5 10.5 11 6l4.5 4.5" fill="none" stroke="#88c43f" stroke-width="2.2"/></svg>
</div>

</body>
</html>
```